Crestline Lending Group Business Cards

We are looking to revamp the current business cards each of our locations uses. We are a lending company that specializes in personal loans, title loans, and tax services. We have locations in New Mexico, Texas, and Oklahoma.

We would like a cleaner, sleeker look while still highlighting what we offer. Title Loans, Personal Loans & Tax Services. We also want to include our referral fee somewhere on the card. We would like to see an English option as well as a Spanish option for the cards.

PLEASE NOTE: Some business cards do not include the employee's name but just the store's location, while others will include both.

These are double-sided business cards, and we would like to see proof if possible. I have included proofs of our current business cards for you to review below, as well as our company logo. Feel free to get creative with the logo, etc! Colors should match the logo; however, you do not need to use all of our logo colors if you don't want to.

```html
<!DOCTYPE html>
<html lang="en">
<head>
<meta charset="utf-8">
<title>Crestline Lending Group – Business Card</title>
<link href="https://fonts.googleapis.com/css2?family=Roboto:wght@400;500;700&display=swap" rel="stylesheet">
<style>
  :root {
    --page-bg: #dedede;
    --card-bg: #ececec;
    --brand-green: #0b4a29;
    --brand-red: #b11c23;
    --brand-red-dark: #7d1218;
    --ink: #111111;
    --white: #ffffff;
  }
  * { margin: 0; padding: 0; box-sizing: border-box; }
  html, body {
    width: 1200px; height: 800px; overflow: hidden;
    background: var(--page-bg);
    font-family: "Roboto", Arial, sans-serif;
  }
  .canvas { position: relative; width: 1200px; height: 800px; }

  .card {
    position: absolute;
    border-radius: 46px;
    overflow: hidden;
    background: var(--card-bg);
  }
  .card-front { left: 140px; top: 261px; width: 453px; height: 259px; }
  .card-back  { left: 623px; top: 263px; width: 446px; height: 255px; }

  .card-art { position: absolute; inset: 0; width: 100%; height: 100%; }

  .brand-name {
    position: absolute;
    color: var(--brand-green);
    font-weight: 700;
    white-space: nowrap;
  }
  .card-front .brand-name { left: 23px; top: 52px; font-size: 15px; }
  .card-back .brand-name {
    left: 0; right: 0; top: 114px;
    text-align: center; font-size: 27px;
  }

  .holder {
    position: absolute; left: 246px; top: 29px; width: 176px;
    text-align: center; color: var(--white);
  }
  .holder-name { font-size: 14px; font-weight: 700; letter-spacing: 0.2px; }
  .holder-title { font-size: 8.5px; margin-top: 3px; }

  .contact-list { position: absolute; left: 23px; top: 167px; list-style: none; }
  .contact-item {
    display: flex; align-items: center; height: 18px;
    font-size: 10.5px; color: var(--ink);
  }
  .contact-icon {
    width: 14px; height: 14px; margin-right: 11px;
    background: var(--brand-red); display: flex; align-items: center; justify-content: center;
  }
  .contact-icon svg { width: 10px; height: 10px; }
  .service-area {
    position: absolute; left: 22px; top: 224px;
    font-size: 10.5px; color: var(--ink);
  }

  .service-list { position: absolute; left: 0; top: 0; list-style: none; }
  .service-item {
    position: absolute; display: flex; align-items: center;
    font-size: 10.5px; color: var(--white); white-space: nowrap;
  }
  .service-item svg { width: 15px; height: 15px; margin-right: 7px; }
</style>
</head>
<body>
<main class="canvas">

  <section class="card card-front" aria-label="Business card front">
    <svg class="card-art" viewBox="0 0 453 259" aria-hidden="true">
      <polygon points="268,0 453,0 453,259 192,259" fill="var(--brand-green)"/>
      <polygon points="229,68 247,68 242,91" fill="var(--brand-red-dark)"/>
      <polygon points="246,23 422,23 422,68 229,68" fill="var(--brand-red)"/>
    </svg>

    <div class="brand-name">Crestline Lending Group</div>

    <div class="holder">
      <div class="holder-name">JOHN DOE</div>
      <div class="holder-title">Founder / CEO</div>
    </div>

    <ul class="contact-list">
      <li class="contact-item">
        <span class="contact-icon"><svg viewBox="0 0 10 10"><path d="M2 1 L3.6 1 L4.3 3 L3.3 3.8 Q4.3 5.9 6.2 6.7 L7 5.7 L9 6.4 L9 8 Q8.5 9 7.5 9 Q1 8.3 1 2.3 Q1 1.2 2 1Z" fill="#fff"/></svg></span>
        123-456-1234
      </li>
      <li class="contact-item">
        <span class="contact-icon"><svg viewBox="0 0 10 10"><rect x="1" y="2.5" width="8" height="5.5" fill="none" stroke="#fff" stroke-width="0.9"/><path d="M1 2.5 L5 5.8 L9 2.5" fill="none" stroke="#fff" stroke-width="0.9"/></svg></span>
        Example@email.com
      </li>
      <li class="contact-item">
        <span class="contact-icon"><svg viewBox="0 0 10 10"><circle cx="5" cy="5" r="3.6" fill="none" stroke="#fff" stroke-width="0.9"/><path d="M1.4 5 H8.6 M5 1.4 Q3 5 5 8.6 M5 1.4 Q7 5 5 8.6" fill="none" stroke="#fff" stroke-width="0.7"/></svg></span>
        www.example.com
      </li>
    </ul>
    <p class="service-area">New Mexico, Texas, and Oklahoma.</p>

    <ul class="service-list">
      <li class="service-item" style="left:246px; top:167px;">
        <svg viewBox="0 0 16 16"><circle cx="8" cy="8" r="7.5" fill="#fff"/><path d="M4.6 8.2 L7 10.4 L11.4 5.8" fill="none" stroke="var(--brand-green)" stroke-width="1.4"/></svg>
        Title Loans
      </li>
      <li class="service-item" style="left:237px; top:193px;">
        <svg viewBox="0 0 16 16"><circle cx="8" cy="8" r="7.5" fill="#fff"/><path d="M4.6 8.2 L7 10.4 L11.4 5.8" fill="none" stroke="var(--brand-green)" stroke-width="1.4"/></svg>
        Personal Loans
      </li>
      <li class="service-item" style="left:228px; top:218px;">
        <svg viewBox="0 0 16 16"><circle cx="8" cy="8" r="7.5" fill="#fff"/><path d="M4.6 8.2 L7 10.4 L11.4 5.8" fill="none" stroke="var(--brand-green)" stroke-width="1.4"/></svg>
        Tax Services
      </li>
    </ul>
  </section>

  <section class="card card-back" aria-label="Business card back">
    <div class="brand-name">Crestline Lending Group</div>
  </section>

</main>
</body>
</html>
```